Law Firm Website

We are looking to update our old, tired and very flat website. We have someone who will code and host the site but we need some design inspiration. The website will consist of no more than 2/3 pages, possibly with pop-ups for information. We already have all the blurb. We would like something distinctive, clean and eye-catching, using the purple and white theme that we already use on our firm stationery. Examples uploaded. Current website URL is www.holtandbrevis.example.

Industry/Entity Type

Law Firm

```html
<!DOCTYPE html>
<html lang="en">
<head>
<meta charset="utf-8">
<title>Holt &amp; Brevis Solicitors</title>
<link rel="stylesheet" href="https://fonts.googleapis.com/css2?family=Lato:wght@400;700&display=swap">
<style>
:root{
  --purple:#5b3f86;
  --purple-band:#6a4c9c;
  --ink:#3b3b3b;
  --muted:#555;
  --rule:#dcdcdc;
  --sidebar:#e6e4e6;
  --btn:#e3e3e3;
  --footer:#393939;
  --footer-text:#e8e8e8;
  --white:#fff;
}
*{margin:0;padding:0;box-sizing:border-box}
html,body{width:830px;height:1200px;overflow:hidden}
body{position:relative;font-family:'Lato',sans-serif;color:var(--ink);background:var(--white)}
.abs{position:absolute}
/* hero */
.hero{left:0;top:0;width:830px;height:330px;background:linear-gradient(180deg,#ececec 0%,#d9d9d9 55%,#cfcfcf 100%)}
.brand{left:0;top:22px;width:830px;text-align:center;font-size:26px;color:var(--purple);letter-spacing:.5px}
.nav{left:250px;top:68px;width:380px;height:28px;border-top:1px solid #d2d2d2;border-bottom:1px solid #d2d2d2;display:flex;justify-content:center;gap:19px;align-items:center;font-size:9px;color:#555;text-transform:uppercase}
.nav .active{color:var(--purple)}
.hero-frame{left:215px;top:150px;width:400px;height:89px}
.hero-title{left:0;top:160px;width:830px;text-align:center;font-size:37px;font-weight:700;color:var(--purple)}
.hero-sub{left:0;top:202px;width:830px;text-align:center;font-size:17px;color:var(--purple)}
/* features */
.feature{top:356px;width:155px;text-align:center}
.feature h2{font-size:16.5px;color:var(--purple);font-weight:700}
.feature hr{width:66px;margin:6px auto 7px;border:0;border-top:1px solid var(--rule)}
.feature p{font-size:8.4px;line-height:14.5px;color:var(--muted);padding:0 6px;height:86px}
.btn{display:inline-block;margin-top:2px;background:var(--btn);border-radius:2px;font-size:7.2px;padding:5px 7px;color:#444;text-transform:uppercase}
.vrule{width:1px;background:var(--rule)}
/* band */
.band{left:0;top:532px;width:830px;height:153px;background:linear-gradient(90deg,#6d559a 0%,#7a5fae 45%,#5f4590 100%)}
.band-text{left:0;top:560px;width:830px;text-align:center;color:var(--white)}
.band-text h2{font-size:15.5px;font-weight:700;margin-bottom:12px}
.band-text p{font-size:9.6px;line-height:16.6px}
/* sidebar */
.sidebar{left:112px;top:716px;width:139px;height:320px;background:var(--sidebar);border-radius:3px;overflow:hidden}
.sidebar h3{background:var(--purple);color:var(--white);font-size:12.5px;line-height:12px;font-weight:700;padding:10px 16px 8px;height:43px}
.sidebar ul{list-style:none;padding:9px 0 0 15px}
.sidebar li{font-size:8.2px;line-height:16.6px;color:#444}
/* people */
.portrait{width:132px;height:132px;border-radius:50%}
.person{top:856px;width:200px;text-align:center}
.person h4{font-size:14px;font-weight:400;color:var(--purple);margin-bottom:4px}
.person p{font-size:7.8px;line-height:10px;font-weight:700;color:#222}
.hrule{left:268px;top:932px;width:450px;height:1px;background:var(--rule)}
.testimonials{left:268px;top:955px;width:450px;text-align:center}
.testimonials h3{font-size:16px;font-weight:700;color:var(--purple);margin-bottom:9px}
.testimonials p{font-size:9.6px;line-height:12px;color:var(--muted);padding:0 50px}
.dots{left:478px;top:1021px;display:flex;gap:2px}
.dots span{width:6px;height:6px;border-radius:50%;background:#cfcfcf}
.dots span.on{background:var(--purple)}
/* footer */
.footer{left:0;top:1062px;width:830px;height:138px;background:var(--footer)}
.office{top:1087px;color:var(--footer-text);font-size:8px;line-height:11.5px}
.office h5{font-size:9.5px;font-weight:700;color:var(--white);margin-bottom:7px}
.office .gap{height:11px}
.badge{left:617px;top:1088px;width:101px;height:36px;background:var(--white);border-radius:3px}
.social{top:1133px;width:21px;height:21px;border-radius:50%;background:#5a5a5a}
.legal{left:500px;top:1162px;width:218px;text-align:right;font-size:7.8px;color:#ddd}
</style>
</head>
<body>
<div class="abs hero" role="img" aria-label="Faded photograph of a stone cathedral with trees"></div>
<div class="abs brand">Holt &amp; Brevis</div>
<nav class="abs nav">
  <span class="active">Home</span><span>Areas of Expertise</span><span>Daniel Holt</span><span>Peter Brevis</span><span>Contact</span>
</nav>
<svg class="abs hero-frame" viewBox="0 0 400 89" fill="none" stroke="#5b3f86" stroke-width="2">
  <polyline points="24,1 1,1 1,88 24,88"/>
  <polyline points="376,1 399,1 399,88 376,88"/>
</svg>
<h1 class="abs hero-title">Holt &amp; Brevis Solicitors,</h1>
<div class="abs hero-sub">For The Service You Deserve</div>

<section class="abs feature" style="left:104px">
  <h2>We Are Different</h2><hr>
  <p>Lorem ipsum dolor sit amet, consectetur adipisicing elit, sed do eiusmod tempor incididunt ut labore et dolore magna aliqua. Ut enim ad minim veniam, quis nostrud exercitation ullamco.</p>
  <span class="btn">Learn More</span>
</section>
<div class="abs vrule" style="left:259px;top:360px;height:142px"></div>
<section class="abs feature" style="left:259px">
  <h2>Our Expertise</h2><hr>
  <p>Sed ut perspiciatis unde omnis iste natus error sit voluptatem accusantium doloremque laudantium, totam rem aperiam, eaque ipsa quae ab illo inventore veritatis et quasi architecto beatae vitae dicta sunt.</p>
  <span class="btn">Learn More</span>
</section>
<div class="abs vrule" style="left:415px;top:360px;height:142px"></div>
<section class="abs feature" style="left:415px">
  <h2>Who We Are</h2><hr>
  <p>Lorem ipsum dolor sit amet, consectetur adipisicing elit, sed do eiusmod tempor incididunt ut labore et dolore magna aliqua. Ut enim ad minim veniam, quis nostrud exercitation ullamco.</p>
  <span class="btn">Learn More</span>
</section>
<div class="abs vrule" style="left:570px;top:360px;height:142px"></div>
<section class="abs feature" style="left:570px">
  <h2>Our Clients</h2><hr>
  <p>Sed ut perspiciatis unde omnis iste natus error sit voluptatem accusantium doloremque laudantium, totam rem aperiam, eaque ipsa quae ab illo inventore veritatis et quasi architecto beatae vitae dicta</p>
  <span class="btn">Learn More</span>
</section>

<div class="abs band" role="img" aria-label="Purple-tinted photograph of a client meeting"></div>
<div class="abs band-text">
  <h2>Holt &amp; Brevis Solicitors</h2>
  <p>HOLT and BREVIS is a firm of solicitors with offices in Hampstead, London and Welwyn, Hertfordshire.</p>
  <p>This firm is authorised and regulated by the Legal Standards Authority, no.310587.</p>
  <p>VAT registered number: 418 2207 56</p>
  <p>Professional rules can be viewed on www.legalstandards.example/code-of-conduct.page.</p>
</div>

<aside class="abs sidebar">
  <h3>Main Areas of Expertise</h3>
  <ul>
    <li>Company Matters</li><li>Commercial Matters</li><li>Commercial Crime</li><li>Litigation/disputes</li><li>insolvency</li><li>residential conveyancing</li><li>Commercial Conveyancing</li><li>Wills &amp; Probate</li><li>Estate Planning</li><li>Powers of attorney</li><li>Care of the Elderly</li><li>Court of Protection</li><li>Divorce/Family</li><li>Pre-nuptial Agreements</li><li>Intellectual Property</li><li>Media Law</li>
  </ul>
</aside>

<div class="abs portrait" style="left:307px;top:717px;background:radial-gradient(circle at 50% 40%,#b9a99a,#6f6358)" role="img" aria-label="Portrait photograph of Daniel Holt"></div>
<div class="abs portrait" style="left:546px;top:717px;background:radial-gradient(circle at 50% 45%,#8a8a8a,#1e1e1e)" role="img" aria-label="Black and white portrait photograph of Peter Brevis"></div>
<div class="abs vrule" style="left:493px;top:716px;height:216px"></div>
<div class="abs person" style="left:273px"><h4>Daniel Holt</h4><p>Peter Brevis has 40 years<br>experience in the law.</p></div>
<div class="abs person" style="left:512px"><h4>Peter Brevis</h4><p>Peter Brevis has 40 years<br>experience in the law.</p></div>
<div class="abs hrule"></div>
<section class="abs testimonials">
  <h3>Client Testimonials</h3>
  <p>"Thanks you, thank you, thank you. Your hard work and dedication has changed my life for the better".</p>
</section>
<div class="abs dots"><span class="on"></span><span></span><span></span><span></span></div>

<footer class="abs footer"></footer>
<div class="abs office" style="left:115px">
  <h5>Daniel Holt</h5>
  22b Linden Row<br>Hampstead<br>London NW3 2QT
  <div class="gap"></div>
  Tel: 0333 555 0142<br>Fax: 020 7946 0318
</div>
<div class="abs office" style="left:216px">
  <h5>Peter Brevis</h5>
  14 Orchard Way<br>Welwyn<br>Hertfordshire AL6 9XY
  <div class="gap"></div>
  Tel: 0845 5550 197<br>Fax: 020 7946 0573
</div>
<div class="abs badge"></div>
<div class="abs social" style="left:643px"></div>
<div class="abs social" style="left:670px"></div>
<div class="abs social" style="left:697px"></div>
<div class="abs legal">Legal Notices &nbsp;|&nbsp; Privacy Policy &nbsp;|&nbsp; © Holt &amp; Brevis</div>
</body>
</html>
```